Quantity Surveying Company Marketing Material

We need a flyer design, Three fold A4 (A4 sheet folded to 3) Two sides
Company: Veltrin Advisory Pty Ltd,
Chartered Quantity Surveyors, Tax Depreciation Consultants
Services: Cost Planning, Estimating, Tax Depreciation, Expert Witness, Bills of Quantities, Tenders, Contract Administration
Highlights: Highly professional service, qualified and experienced staff, quality of service and accuracy
Our motto: Quality service at an affordable price
Our theme: Your partner in construction cost management
Company colour scheme: Blue
Website: www.veltrinadvisory.com.au

Target Market(s)

Architects, Builders, Construction companies, Home owner builders, Investment property owners (Mainly Residential projects such as houses, townhouses, apartments. In addition Retail and Civil infrastructure projects)

Industry/Entity Type

It Company

Colors
3176b5
886aae
33b8a4
fac994

Requirements
Must have
• Senior staff are
• Professional members of Imperial Guild of Licensed Assessors (IGLA)
• Professional members of Federated College of Building Estimators (FCBE)
• Professional members of Society of Structural Planners (SOSP)
• Registered members of Fiscal Advisers Panel (FAP)
• (If this is too wordy, short form names with logos will suffice. But I do not have the SOSP logo)
Nice to have
• Blue and purple colours
• Above mentioned IGLA logo, FCBE logo and FAP logo
Should not have
• No to any funny stuff non-professional stuff.

```html
<!DOCTYPE html>
<html lang="en">
<head>
<meta charset="utf-8">
<title>Veltrin Advisory – Tri-fold Flyer</title>
<link rel="stylesheet" href="https://fonts.googleapis.com/css2?family=Roboto+Condensed:wght@400;700&display=swap">
<style>
  :root {
    --blue: #2f70b3;
    --purple: #7a62aa;
    --navy: #14284a;
    --mist: #d4d7df;
    --rule: #111111;
    --paper: #ffffff;
    --sky-top: #c9ced6;
    --sky-bottom: #6f7a86;
  }
  * { margin: 0; padding: 0; box-sizing: border-box; }
  html, body { width: 1200px; height: 1000px; overflow: hidden; background: var(--paper); }
  body { font-family: "Roboto Condensed", "Arial Narrow", sans-serif; font-weight: 700; color: var(--blue); }
  .flyer { position: relative; width: 1200px; height: 1000px; }
  .rule { position: absolute; left: 0; width: 1200px; height: 3px; background: var(--rule); }
  .rule--top { top: 72px; }
  .rule--bottom { top: 924px; }

  .skyline { position: absolute; left: 0; top: 0; }

  .panel-about { position: absolute; left: 15px; top: 92px; width: 380px; }
  .heading { color: var(--purple); font-size: 27px; line-height: 32px; letter-spacing: -0.2px; }
  .intro { font-size: 17px; line-height: 24px; margin-top: 6px; }
  .memberships { list-style: none; margin-top: 14px; }
  .memberships li { font-size: 17px; line-height: 24px; margin-bottom: 24px; position: relative; padding-left: 5px; }
  .memberships li::before, .staff li::before {
    content: ""; position: absolute; left: -9px; top: 13px; width: 5px; height: 5px;
    border-radius: 50%; background: var(--purple);
  }
  .heading--staff { margin-top: -12px; }
  .staff { list-style: none; margin-top: 14px; width: 330px; }
  .staff li { font-size: 17px; line-height: 24px; margin-bottom: 24px; position: relative; padding-left: 4px; }

  .motto { position: absolute; left: 395px; top: 192px; width: 400px; text-align: center;
    font-size: 37px; line-height: 53px; }
  .contact { position: absolute; left: 460px; top: 410px; width: 290px; text-align: center; }
  .contact .heading { margin-bottom: 26px; padding-right: 20px; }
  .contact address { font-style: normal; font-size: 19px; line-height: 27px; }

  .brand-disc { position: absolute; left: 815px; top: 118px; width: 340px; height: 340px;
    border-radius: 50%; background: var(--mist); }
  .brand-name { position: absolute; left: 840px; top: 200px; width: 300px; text-align: center;
    color: var(--navy); font-size: 60px; line-height: 76px; }
  .tagline { position: absolute; left: 830px; top: 448px; width: 330px; text-align: center;
    font-size: 38px; line-height: 53px; }
</style>
</head>
<body>
<main class="flyer">
  <div class="rule rule--top"></div>

  <svg class="skyline" width="1200" height="1000" viewBox="0 0 1200 1000" role="img" aria-label="Illustrated city skyline of high-rise office towers in grey and blue tones">
    <defs>
      <linearGradient id="skyline-tone" x1="0" y1="0" x2="0" y2="1">
        <stop offset="0" stop-color="var(--sky-top)"/>
        <stop offset="1" stop-color="var(--sky-bottom)"/>
      </linearGradient>
    </defs>
    <rect x="0" y="720" width="1200" height="204" fill="url(#skyline-tone)"/>
  </svg>

  <div class="brand-disc"></div>
  <div class="brand-name">VELTRIN<br>Advisory</div>

  <section class="panel-about">
    <h2 class="heading">Who we are:</h2>
    <p class="intro">Veltrin Advisory is a Chartered Quantity Surveying Consultancy in Sydney offering a range of skills across New South Wales. We are professional members of:</p>
    <ul class="memberships">
      <li>Federated College of Building Estimators (FCBE)</li>
      <li>Imperial Guild of Licensed Assessors (IGLA)</li>
      <li>Society of Structural Planners (SOSP)</li>
      <li>Fiscal Advisers Panel of Australia (FAP)</li>
    </ul>
    <h2 class="heading heading--staff">Senior staff:</h2>
    <ul class="staff">
      <li>Professional members of Imperial Guild of Licensed Assessors (IGLA)</li>
      <li>Professional members of Federated College of Building Estimators (FCBE)</li>
      <li>Professional members of Society of Structural Planners (SOSP)</li>
      <li>Registered members of Fiscal Advisers Panel (FAP)</li>
    </ul>
  </section>

  <p class="motto">Quality service<br>at an affordable price.</p>

  <section class="contact">
    <h2 class="heading">Contact us</h2>
    <address>
      Veltrin Advisory Pty Ltd<br>
      48 Harrowgate Street<br>
      Linfield Park, NSW 2071<br>
      (02) 8123 4560, (02) 9870 1245<br>
      info@veltrinadvisory.com.au<br>
      www.veltrinadvisory.com.au
    </address>
  </section>

  <p class="tagline">Your partner in<br>construction<br>cost management.</p>

  <div class="rule rule--bottom"></div>
</main>
</body>
</html>
```